Business card for a new innovative and professional lawn care business

We need a business card design for a new lawn care business in Halifax NS Canada. We offer lawn services in Halifax & Bedford. Our services offered include lawn care, garden services, and property maintenance. We take pride in our work and are experienced at what we do. I would like to see a design that is double sided. On the backside I would like the something simple (maybe my logo preferably on blackround (linked below) with website link, Facebook page or something). The front I want to include contact info:
Darren Maple
phone 902-555-0148
email - darrensyardworks.ca
facebook - Facebook.com/darrensyardworks
Instagram maybe ? - instagram.com/darrenyardworks
Serving Halifax and Bedford for 5 years?
I don't want it to have too much information as I will be passing them out in aim to visit website, or call !
We do want it to include lawn care, garden services and property maintenance.
Basic, catchy, and modern looking !
Logo attached below !

Target Market(s)

Passing business cards to everyone I meet or interact with.

Industry/Entity Type

Lawn Care

Contact Information for Business Card

Double sided with some basic information, with catchy colours and easy to look at.

Font styles to use
Sans Serif

Requirements
Must have
• Must be double sided and have :
• Name, Phone, Email, FB, Website, and 3 main services offered - lawn care, property maintenance, garden services
Nice to have
• Would be nice to have instagram link if it goes well on there
Should not have
• Don't want too much writing or images that are distracting

```html
<!DOCTYPE html>
<html lang="en">
<head>
<meta charset="utf-8">
<title>Darren's Yard Works – Business Card</title>
<link href="https://fonts.googleapis.com/css2?family=Lato:wght@400;700;900&display=swap" rel="stylesheet">
<style>
  :root {
    --bg: #2b2b2b;
    --lime: #86c23a;
    --lime-dark: #6fa82a;
    --forest: #1f6b2e;
    --ink: #333a40;
    --paper: #ffffff;
    --paper-shade: #f2f3f1;
  }
  * { box-sizing: border-box; margin: 0; padding: 0; }
  html, body {
    width: 1200px; height: 873px; overflow: hidden;
    background: var(--bg);
    font-family: "Lato", sans-serif;
  }
  .stage {
    width: 1200px; height: 873px;
    display: flex; flex-direction: column;
    align-items: center; justify-content: center; gap: 56px;
  }
  .card {
    position: relative;
    width: 560px; height: 320px;
    border-radius: 18px;
    overflow: hidden;
    background: linear-gradient(135deg, var(--paper) 0%, var(--paper-shade) 100%);
    display: flex;
  }

  /* back side */
  .card-back .band {
    width: 70px; background: var(--lime); position: relative;
  }
  .card-back .band::after {
    content: ""; position: absolute; top: 0; bottom: 0; width: 14px;
    border-left: 2px solid var(--paper); border-right: 2px solid var(--paper);
  }
  .card-back .band-left::after { right: 8px; }
  .card-back .band-right::after { left: 8px; }
  .card-back .band::before {
    content: ""; position: absolute; top: 0; bottom: 0; width: 2px; background: var(--paper);
  }
  .card-back .band-left::before { right: 14px; }
  .card-back .band-right::before { left: 14px; }
  .card-back .center {
    flex: 1; display: flex; align-items: center; justify-content: center;
  }

  .brand {
    display: flex; align-items: center; gap: 12px;
    color: var(--forest); font-weight: 900; letter-spacing: 1px;
    text-transform: uppercase; line-height: 1;
  }
  .brand-mark { width: 18px; height: 18px; border-radius: 50%; background: var(--forest); flex: none; }
  .card-back .brand { font-size: 34px; }

  /* front side */
  .card-front .panel {
    width: 232px; background: var(--lime); padding: 44px 0 0 22px; position: relative;
  }
  .card-front .stripes {
    width: 22px; position: relative;
    background: var(--paper);
    border-left: 4px solid var(--lime);
  }
  .card-front .stripes::before,
  .card-front .stripes::after {
    content: ""; position: absolute; top: 0; bottom: 0; width: 4px; background: var(--lime);
  }
  .card-front .stripes::before { left: 6px; }
  .card-front .stripes::after { left: 14px; }

  .name { font-size: 20px; font-weight: 900; color: var(--ink); }
  .role { font-size: 11px; color: var(--paper); margin: 4px 0 0 18px; }

  .contacts { list-style: none; margin-top: 44px; display: flex; flex-direction: column; gap: 6px; }
  .contacts li { display: flex; align-items: center; gap: 10px; color: var(--paper); font-size: 12.5px; }
  .icon {
    width: 24px; height: 24px; background: var(--paper); border-radius: 2px;
    display: flex; align-items: center; justify-content: center; flex: none;
  }
  .icon svg { width: 15px; height: 15px; fill: none; stroke: var(--lime-dark); stroke-width: 2; }
  .icon-plain span { width: 12px; height: 12px; background: var(--lime); border-radius: 2px; }

  .card-front .side {
    flex: 1; display: flex; flex-direction: column; align-items: center;
    justify-content: space-between; padding: 96px 16px 40px;
  }
  .card-front .brand { font-size: 25px; }
  .services { font-size: 11.5px; font-weight: 700; color: var(--ink); }
</style>
</head>
<body>
<main class="stage">

  <section class="card card-back" aria-label="Card back">
    <div class="band band-left"></div>
    <div class="center">
      <div class="brand"><span class="brand-mark"></span>Darren's Yard Works</div>
    </div>
    <div class="band band-right"></div>
  </section>

  <section class="card card-front" aria-label="Card front">
    <div class="panel">
      <h1 class="name">Darren Maple</h1>
      <p class="role">Owner / Director</p>
      <ul class="contacts">
        <li><span class="icon"><svg viewBox="0 0 24 24"><path d="M5 3h4l2 5-3 2a12 12 0 0 0 6 6l2-3 5 2v4a2 2 0 0 1-2 2A17 17 0 0 1 3 5a2 2 0 0 1 2-2z"/></svg></span>902-555-0148</li>
        <li><span class="icon"><svg viewBox="0 0 24 24"><rect x="3" y="5" width="18" height="14"/><path d="M3 5l9 8 9-8"/></svg></span>me@darrensyardworks.ca</li>
        <li><span class="icon"><svg viewBox="0 0 24 24"><circle cx="12" cy="12" r="9"/><path d="M3 12h18M12 3c3 3 3 15 0 18M12 3c-3 3-3 15 0 18"/></svg></span>www.darrensyardworks</li>
        <li><span class="icon icon-plain"><span></span></span>/darrensyardworks</li>
        <li><span class="icon icon-plain"><span></span></span>/darrenyardworks</li>
      </ul>
    </div>
    <div class="stripes"></div>
    <div class="side">
      <div class="brand"><span class="brand-mark"></span>Darren's Yard Works</div>
      <p class="services">Lawn Care, Property Maintenance, Garden Services</p>
    </div>
  </section>

</main>
</body>
</html>
```